Restaurant needs a vertical banner for fried catfish

Our restaurant is looking for an eye-catching 78.75in. x 36in. vertical physical banner ad for our fried catfish. Photos for the fried catfish will be provided as a reference but we will also accept anything similar to the photo. We will be using the following as our receptacle: https://www.plankoria.example/banner-stand/retractable-banner-stands/
The design must incorporate the following flavor texts:
Fried Catfish
Always Fresh!
Made from Scratch
Hand-cut Fillets
The Best Catfish in Texas
Served with fries, hush puppies, and a 32oz fountain drink
Also available by the pound!
The final design should be creative, professional, and eye-catching for customers.
Updates
Colors
Designer to choose colors to be used in the design.
Requirements
Must have
- We are open to any and all design elements, albeit the 'flavor texts' should not overpower, but complement the fried catfish photo. 'Fried Catfish' can be used in lieu of a main title/logo.
Nice to have
- Transparent or textured backgrounds that can encompass any or all part of the banner such as a cutting board, shadows, abstract, etc to show depth are a plus.
- Use of vectors or objects such as ribbons or shapes to encapsulate the 'flavor texts' are also encouraged.

```html
<!DOCTYPE html>
<html lang="en">
<head>
<meta charset="utf-8">
<title>Fried Catfish Banner</title>
<link rel="stylesheet" href="https://fonts.googleapis.com/css2?family=Arvo:ital,wght@0,700;1,700&family=Oswald:wght@500&display=swap">
<style>
  :root {
    --orange: #f7a21b;
    --orange-deep: #f39a12;
    --green: #0f7354;
    --green-title: #15654e;
    --ink: #1c1a17;
    --white: #ffffff;
    --photo-warm: #b87a35;
    --photo-light: #e9d3a8;
  }
  html, body {
    margin: 0;
    padding: 0;
    width: 1200px;
    height: 2624px;
    overflow: hidden;
    background: var(--green);
  }
  .banner {
    position: relative;
    width: 1200px;
    height: 2624px;
    overflow: hidden;
  }
  .banner-shapes {
    position: absolute;
    inset: 0;
    display: block;
  }
  .headline {
    position: absolute;
    left: 0;
    top: 0;
    width: 1200px;
    text-align: center;
    transform-origin: 0 0;
    font-family: "Arvo", Georgia, serif;
    font-weight: 700;
    margin: 0;
  }
  .headline-title {
    font-size: 122px;
    line-height: 1;
    color: var(--green-title);
    letter-spacing: 2px;
    transform: translate(0, 200px) rotate(-14.2deg);
    transform-origin: 586px 60px;
  }
  .headline-tagline {
    font-size: 44px;
    line-height: 1;
    color: var(--ink);
    transform: translate(14px, 326px) rotate(-14.2deg);
    transform-origin: 586px 22px;
  }
  .feature {
    position: absolute;
    left: 0;
    width: 1200px;
    margin: 0;
    text-align: center;
    font-family: "Oswald", "Arial Narrow", sans-serif;
    font-weight: 500;
    font-size: 66px;
    line-height: 90px;
    color: var(--white);
    text-transform: uppercase;
    letter-spacing: 0.5px;
  }
  .footer-note {
    position: absolute;
    left: 0;
    top: 2466px;
    width: 1200px;
    height: 158px;
    margin: 0;
    display: flex;
    align-items: center;
    justify-content: center;
    font-family: "Arvo", Georgia, serif;
    font-style: italic;
    font-weight: 700;
    font-size: 54px;
    color: var(--ink);
    text-transform: uppercase;
  }
</style>
</head>
<body>
<main class="banner">
  <svg class="banner-shapes" width="1200" height="2624" viewBox="0 0 686 1500" preserveAspectRatio="none" xmlns="http://www.w3.org/2000/svg">
    <defs>
      <linearGradient id="photoTone" x1="0" y1="0" x2="1" y2="1">
        <stop offset="0" stop-color="var(--photo-light)"/>
        <stop offset="0.45" stop-color="var(--photo-warm)"/>
        <stop offset="1" stop-color="#d9c9a8"/>
      </linearGradient>
    </defs>
    <rect class="field-orange" x="0" y="0" width="686" height="330" fill="var(--orange)"/>
    <rect class="field-green" x="0" y="560" width="686" height="940" fill="var(--green)"/>
    <polygon class="photo-area" role="img" aria-label="Photo of golden cornmeal-fried catfish fillets with fries, hush puppies and tartar sauce on a white plate" points="0,318 686,163 686,566 0,716" fill="url(#photoTone)"/>
    <polygon class="stripe-green" points="0,298 686,143 686,166 0,321" fill="var(--green)"/>
    <polygon class="stripe-orange" points="0,708 686,556 686,578 0,732" fill="var(--orange)"/>

    <g class="cutlery" fill="var(--orange)">
      <g transform="translate(0,733)">
        <path d="M325,-17 h30 v2 h-28 v3 h28 v2 h-28 v3 h28 v2 h-28 v3 h28 v2 h-30 z"/>
        <path d="M353,-12 q8,-6 16,-1 h76 v5 h-76 q-8,5 -16,-1 z"/>
        <ellipse cx="306" cy="15" rx="17" ry="9"/>
        <path d="M320,12 h90 v6 h-90 z"/>
      </g>
      <g transform="translate(0,880)">
        <path d="M325,-17 h30 v2 h-28 v3 h28 v2 h-28 v3 h28 v2 h-28 v3 h28 v2 h-30 z"/>
        <path d="M353,-12 q8,-6 16,-1 h76 v5 h-76 q-8,5 -16,-1 z"/>
        <ellipse cx="306" cy="15" rx="17" ry="9"/>
        <path d="M320,12 h90 v6 h-90 z"/>
      </g>
      <g transform="translate(0,1040)">
        <path d="M325,-17 h30 v2 h-28 v3 h28 v2 h-28 v3 h28 v2 h-28 v3 h28 v2 h-30 z"/>
        <path d="M353,-12 q8,-6 16,-1 h76 v5 h-76 q-8,5 -16,-1 z"/>
        <ellipse cx="306" cy="15" rx="17" ry="9"/>
        <path d="M320,12 h90 v6 h-90 z"/>
      </g>
      <g transform="translate(0,1188)">
        <path d="M325,-17 h30 v2 h-28 v3 h28 v2 h-28 v3 h28 v2 h-28 v3 h28 v2 h-30 z"/>
        <path d="M353,-12 q8,-6 16,-1 h76 v5 h-76 q-8,5 -16,-1 z"/>
        <ellipse cx="306" cy="15" rx="17" ry="9"/>
        <path d="M320,12 h90 v6 h-90 z"/>
      </g>
    </g>

    <rect class="footer-bar" x="0" y="1410" width="686" height="90" fill="var(--orange)"/>
  </svg>

  <h1 class="headline headline-title">FRIED CATFISH</h1>
  <p class="headline headline-tagline">ALWAYS FRESH!</p>

  <p class="feature" style="top:1368px">Made from Scratch</p>
  <p class="feature" style="top:1625px">Hand-Cut Fillets</p>
  <p class="feature" style="top:1896px">The Best Catfish in Texas</p>
  <p class="feature" style="top:2167px">Served with Fries, Hush Puppies</p>
  <p class="feature" style="top:2272px">and a 32oz Fountain Drink</p>

  <p class="footer-note">Also available by the pound!</p>
</main>
</body>
</html>
```